Harborline Crest Insurance Services

we are a high end insurance agency we specialize on Auto | Home | Business | Life looking for something professional and luxuries at the same time. if you guys need anything else please let me know.

Auto | Home | Business | Life must be under logo on the back with black background.

i want the back part to be black with our gold logo on it.

Target Market(s)

Auto | Home | Business | Life

Industry/Entity Type

Insurance Broker

Contact Information for Business Card

My logo is gold so a black in the back would be nice.

Font styles to use
Serif

Colors
000000

Requirements
Must have
• Big logo on the back with black background.

```html
<!DOCTYPE html>
<html lang="en">
<head>
<meta charset="utf-8">
<title>Harborline Crest Insurance Services – Business Card</title>
<link rel="stylesheet" href="https://fonts.googleapis.com/css2?family=Cinzel:wght@600&family=Arimo:wght@400;700&display=swap">
<style>
  :root {
    --gold: #e8b419;
    --gold-deep: #c99a0e;
    --ink: #111111;
    --card-black: #050505;
    --card-white: #f7f7f7;
    --grey-text: #9a9a9a;
    --stage: #3a3a3a;
  }
  * { box-sizing: border-box; margin: 0; padding: 0; }
  html, body { width: 1200px; height: 997px; overflow: hidden; }
  body { background: var(--stage); font-family: "Arimo", Arial, sans-serif; position: relative; }

  .card { position: absolute; width: 560px; height: 320px; overflow: hidden; }

  /* Back side */
  .card-back { left: 90px; top: 90px; background: var(--card-black); display: flex; flex-direction: column; align-items: center; justify-content: center; }
  .back-mark { width: 44px; height: 44px; border-radius: 50%; background: var(--gold); margin-bottom: 22px; }
  .back-name { font-family: "Cinzel", Georgia, serif; font-weight: 600; color: var(--gold); text-align: center; line-height: 1.15; }
  .back-name .line-main { display: block; font-size: 38px; letter-spacing: 1px; }
  .back-name .line-sub { display: block; font-size: 17px; letter-spacing: 5px; }
  .back-services { margin-top: 22px; font-size: 14px; letter-spacing: 3px; color: var(--gold); }
  .back-services .divider { color: var(--grey-text); margin: 0 6px; }

  /* Front side */
  .card-front { left: 550px; top: 480px; background: var(--card-white); }
  .front-logo { position: absolute; left: 150px; top: 34px; display: flex; align-items: center; gap: 12px; }
  .front-logo .mark { width: 30px; height: 30px; border-radius: 50%; background: var(--gold); }
  .front-logo .name { font-family: "Cinzel", Georgia, serif; font-weight: 600; color: var(--gold); line-height: 1.1; }
  .front-logo .name .line-main { display: block; font-size: 21px; }
  .front-logo .name .line-sub { display: block; font-size: 10px; letter-spacing: 3px; }
  .rule { position: absolute; left: 28px; right: 28px; top: 118px; height: 2px; background: var(--gold); }
  .person { position: absolute; left: 30px; top: 128px; }
  .person .full-name { font-weight: 700; font-size: 16px; color: var(--gold); letter-spacing: .5px; }
  .person .role { font-size: 13px; color: var(--ink); margin-top: 3px; }
  .contacts { position: absolute; left: 30px; top: 196px; list-style: none; }
  .contacts li { display: flex; align-items: center; gap: 10px; font-size: 14px; color: var(--ink); height: 24px; }
  .contacts .icon { width: 16px; height: 16px; border-radius: 50%; background: var(--ink); display: flex; align-items: center; justify-content: center; }
  .office { position: absolute; right: 30px; top: 132px; text-align: right; font-size: 13px; color: var(--ink); line-height: 1.35; }
  .office .company { font-weight: 700; color: var(--gold); }
  .front-band { position: absolute; left: 0; bottom: 0; width: 560px; height: 80px; }
  .website { position: absolute; right: 30px; bottom: 26px; font-weight: 700; font-size: 13px; letter-spacing: 4px; color: var(--ink); }
</style>
</head>
<body>

<section class="card card-back" aria-label="Card back">
  <div class="back-mark"></div>
  <h1 class="back-name"><span class="line-main">Harborline Crest</span><span class="line-sub">Insurance Services</span></h1>
  <p class="back-services">AUTO<span class="divider">|</span>HOME<span class="divider">|</span>BUSINESS<span class="divider">|</span>LIFE</p>
</section>

<section class="card card-front" aria-label="Card front">
  <div class="front-logo">
    <span class="mark"></span>
    <p class="name"><span class="line-main">Harborline Crest</span><span class="line-sub">Insurance Services</span></p>
  </div>
  <div class="rule"></div>

  <div class="person">
    <p class="full-name">MARCUS DELVANE</p>
    <p class="role">COO (GLOBAL)</p>
  </div>

  <ul class="contacts">
    <li><span class="icon"><svg width="10" height="10" viewBox="0 0 10 10"><path d="M2 1h2l1 2-1 1a5 5 0 0 0 2 2l1-1 2 1v2l-1 1C4 9 1 6 1 2z" fill="#e8b419"/></svg></span>+61 3 9000 1234</li>
    <li><span class="icon"><svg width="10" height="10" viewBox="0 0 10 10"><rect x="3" y="1" width="4" height="8" rx="1" fill="#e8b419"/></svg></span>+61 400 555 218</li>
    <li><span class="icon"><svg width="10" height="10" viewBox="0 0 10 10"><rect x="1" y="2.5" width="8" height="5" fill="#e8b419"/><path d="M1 2.5l4 3 4-3" stroke="#111" stroke-width=".8" fill="none"/></svg></span>marcus@harborline-crest.com</li>
  </ul>

  <address class="office" style="font-style:normal">
    <span class="company">Harborline Crest Pvt Ltd</span><br>
    Level 5, 42 Wattle Street<br>
    Melbourne VIC 3000 Australia
  </address>

  <svg class="front-band" viewBox="0 0 560 80" aria-hidden="true">
    <path d="M0 66 L420 50 Q440 49 448 40 Q460 24 500 22 L560 20 L560 80 L0 80 Z" fill="#c99a0e"/>
    <path d="M0 62 L400 46 Q420 45 428 36 L440 22 Q452 12 490 10 L560 8 L560 80 L0 80 L0 70 Z" fill="#e8b419" transform="translate(0 0)"/>
    <path d="M0 58 L395 44 Q412 43 418 36 L423 30 L420 38 Q414 48 398 49 L0 64 Z" fill="#111"/>
  </svg>
  <p class="website">WWW.HCIS.COM</p>
</section>

</body>
</html>
```